Kettle Ledger Business Card design

We need a stand out business card design for Accounting practice based in Australia specialising in pubs, clubs and hotels. We help venues maximise margins, create time and manage cashflow. One club we have been working with for the last 6 months has increased revenue by 3% and margin by 5% in this time frame. We have a back office outsourced system that costs less than having a full time employee and also allows the venues the added benefit of:<br/>-using the office space to become a revenue generating opportunity. <br/>-a complete system to enhance governance, accountability and efficiency within their operation<br/>-52 weeks cover so no hassle to cover annual/sick .. leave<br/><br/>We would like to see designs that use the colours of our logo (green & blue).
Target Market(s)
Australian Pubs, Clubs & Hotels abookkeeping, accounting and tax services
Industry/Entity Type
Accountant
Contact Information for Business Card
Miriam Oakley CPA
Principal
Accountant Tax Agent
Miriam@KettleLedger-example.com.au
0418693142
www.kettleledger-example.com.au
Accounting / Payroll / Tax / SMSF / Technology
Colors
Designer to choose colors to be used in the design.
Look and feel
Each slider illustrates characteristics of the customer's brand and the style your logo design should communicate.

```html
<!DOCTYPE html>
<html lang="en">
<head>
<meta charset="utf-8">
<title>Kettle Ledger Business Card</title>
<link href="https://fonts.googleapis.com/css2?family=Lato:wght@400;700;900&display=swap" rel="stylesheet">
<style>
  :root {
    --brand-blue: #233e8f;
    --brand-green: #137a3a;
    --card-white: #ffffff;
    --ink: #3a3a3a;
    --backdrop: #2b2b2d;
  }
  * { margin: 0; padding: 0; box-sizing: border-box; }
  html, body { width: 1200px; height: 900px; overflow: hidden; }
  body {
    background: var(--backdrop);
    font-family: "Lato", sans-serif;
    position: relative;
  }
  .card {
    position: absolute;
    width: 620px;
    height: 354px;
    background: var(--card-white);
    border-radius: 22px;
    overflow: hidden;
    box-shadow: 0 18px 40px rgba(0,0,0,0.45);
  }
  .card--front { left: 60px; top: 70px; }
  .card--back { left: 520px; top: 476px; }

  .contact-panel { position: absolute; inset: 0; width: 100%; height: 100%; }

  .wordmark {
    display: flex;
    align-items: center;
    gap: 14px;
    color: var(--brand-blue);
    font-weight: 900;
    font-size: 46px;
    letter-spacing: -0.5px;
    line-height: 1;
    white-space: nowrap;
  }
  .wordmark__dot {
    width: 34px; height: 34px;
    border-radius: 50%;
    background: var(--brand-green);
    flex: none;
  }
  .card--front .wordmark { position: absolute; left: 38px; top: 112px; font-size: 40px; }
  .card--back .wordmark { position: absolute; left: 50%; top: 50%; transform: translate(-50%, -50%); font-size: 54px; }
  .card--back .wordmark__dot { width: 42px; height: 42px; }

  .services {
    position: absolute;
    left: 40px;
    bottom: 30px;
    list-style: none;
    color: var(--ink);
    font-size: 15px;
    line-height: 1.3;
    letter-spacing: 0.4px;
  }
  .services li:nth-child(2) { padding-left: 10px; }
  .services li:nth-child(3) { padding-left: 20px; }
  .services li:nth-child(4) { padding-left: 30px; }
  .services li:nth-child(5) { padding-left: 40px; }

  .contact {
    position: absolute;
    right: 28px;
    bottom: 34px;
    text-align: right;
    color: var(--card-white);
    white-space: nowrap;
  }
  .contact__name { font-weight: 900; font-size: 18px; letter-spacing: 0.2px; }
  .contact__role { font-size: 14px; margin-top: 2px; margin-bottom: 18px; }
  .contact__line {
    display: flex;
    justify-content: flex-end;
    align-items: center;
    gap: 7px;
    font-size: 12px;
    margin-top: 5px;
  }
  .contact__line svg { width: 12px; height: 12px; flex: none; fill: var(--card-white); }
</style>
</head>
<body>

  <section class="card card--front">
    <svg class="contact-panel" viewBox="0 0 620 354" preserveAspectRatio="none" aria-hidden="true">
      <path d="M560 0 C590 110 300 150 320 354 L620 354 L620 0 Z" fill="var(--brand-green)"/>
      <path d="M574 0 C604 110 314 150 334 354 L620 354 L620 0 Z" fill="var(--card-white)"/>
      <path d="M580 0 C610 110 320 150 340 354 L620 354 L620 0 Z" fill="var(--brand-blue)"/>
    </svg>

    <div class="wordmark"><span class="wordmark__dot"></span>Kettle Ledger</div>

    <ul class="services">
      <li>Accounting</li>
      <li>Payroll</li>
      <li>Tax</li>
      <li>SMSF</li>
      <li>Technology</li>
    </ul>

    <div class="contact">
      <div class="contact__name">Miriam Oakley Cpa</div>
      <div class="contact__role">Principal</div>
      <div class="contact__line">0418693142
        <svg viewBox="0 0 24 24"><path d="M6.6 10.8a15 15 0 0 0 6.6 6.6l2.2-2.2c.3-.3.7-.4 1-.2 1.1.4 2.3.6 3.6.6.6 0 1 .4 1 1V20c0 .6-.4 1-1 1A17 17 0 0 1 3 4c0-.6.4-1 1-1h3.5c.6 0 1 .4 1 1 0 1.3.2 2.5.6 3.6.1.3 0 .7-.2 1z"/></svg>
      </div>
      <div class="contact__line">Miriam@KettleLedger-example.com.au
        <svg viewBox="0 0 24 24"><path d="M2 5h20v14H2z M3.5 6.5 12 13l8.5-6.5" stroke="var(--brand-blue)" stroke-width="1.6"/></svg>
      </div>
      <div class="contact__line">www.kettleledger-example.com.au
        <svg viewBox="0 0 24 24"><circle cx="12" cy="12" r="10"/><path d="M2 12h20M12 2c3 3 3 17 0 20M12 2c-3 3-3 17 0 20" stroke="var(--brand-blue)" stroke-width="1.5" fill="none"/></svg>
      </div>
    </div>
  </section>

  <section class="card card--back">
    <div class="wordmark"><span class="wordmark__dot"></span>Kettle Ledger</div>
  </section>

</body>
</html>
```